Letterhead Design Project

Attached is our new Logo and a copy of our old letter head
Looking to rebrand with our new logo

Reason: I want to show a business card design

Industry/Entity Type

Film Production

Colors

Designer to choose colors to be used in the design.

Requirements
Must have
• The information on the old letterhead

```html
<!DOCTYPE html>
<html lang="en">
<head>
<meta charset="utf-8">
<title>KAVRO International Letterhead</title>
<link href="https://fonts.googleapis.com/css2?family=Open+Sans:wght@400;600;700&display=swap" rel="stylesheet">
<style>
  :root {
    --backdrop: #ececec;
    --paper: #ffffff;
    --band-top: #62b8ef;
    --band-fade: #ffffff;
    --blue: #3aa6ea;
    --deep-blue: #1f6fd1;
    --navy: #1c3a6b;
    --ink: #1a1a1a;
  }
  * { margin: 0; padding: 0; box-sizing: border-box; }
  html, body {
    width: 1200px; height: 795px; overflow: hidden;
    background: var(--backdrop);
    font-family: "Open Sans", Arial, sans-serif;
  }
  .letterhead {
    position: absolute; left: 330px; top: 16px;
    width: 540px; height: 763px;
    background: var(--paper);
    box-shadow: 0 4px 18px rgba(0,0,0,.18);
    overflow: hidden;
  }
  .header-band, .footer-band { position: absolute; left: 0; width: 100%; }
  .header-band {
    top: 0; height: 240px;
    background: linear-gradient(to bottom, var(--band-top) 0%, #a9dbf8 55%, var(--band-fade) 100%);
  }
  .footer-band {
    bottom: 0; height: 270px;
    background: linear-gradient(to top, var(--band-top) 0%, #a9dbf8 40%, var(--band-fade) 100%);
  }

  .contact {
    position: absolute; top: 26px; right: 30px;
    text-align: right; font-size: 10px; line-height: 15px; color: var(--navy);
  }
  .contact li { list-style: none; display: flex; justify-content: flex-end; align-items: center; gap: 5px; }
  .contact svg { width: 9px; height: 9px; }

  .brand { position: absolute; left: 34px; top: 150px; }
  .brand-name {
    display: flex; align-items: center; gap: 7px;
    font-size: 20px; font-weight: 700; color: var(--navy); letter-spacing: .5px;
  }
  .brand-dot { width: 11px; height: 11px; border-radius: 50%; background: var(--deep-blue); }
  .tagline {
    margin-top: 3px; font-size: 8.5px; letter-spacing: .6px;
    color: var(--navy); text-transform: uppercase;
  }

  .footer-info {
    position: absolute; right: 30px; bottom: 96px;
    text-align: right; color: var(--ink);
  }
  .divisions { font-size: 11px; font-weight: 600; line-height: 17px; }
  .divisions .sep {
    display: inline-block; width: 6px; height: 6px; border-radius: 50%;
    background: var(--blue); margin: 0 6px; vertical-align: middle;
  }
  .parent { font-size: 10.5px; margin-top: 3px; }
  .registration { font-size: 11px; font-weight: 700; margin-top: 2px; }
</style>
</head>
<body>
  <main class="letterhead">
    <div class="header-band" role="img" aria-label="Soft blue gradient header band"></div>

    <ul class="contact">
      <li><svg viewBox="0 0 10 10"><path d="M5 1a3 3 0 0 1 3 3c0 2-3 5-3 5S2 6 2 4a3 3 0 0 1 3-3z" fill="#1c3a6b"/></svg>P.O. Box 482 Larkhill QLD 4390</li>
      <li><svg viewBox="0 0 10 10"><path d="M5 1a3 3 0 0 1 3 3c0 2-3 5-3 5S2 6 2 4a3 3 0 0 1 3-3z" fill="#1c3a6b"/></svg>P.O. Box 317 Morrow NSW 2195</li>
      <li><svg viewBox="0 0 10 10"><circle cx="5" cy="5" r="4" stroke="#1c3a6b" fill="none"/><path d="M3.5 3.5l1 1.5 1.5 1" stroke="#1c3a6b" fill="none"/></svg>0400 118 275</li>
      <li><svg viewBox="0 0 10 10"><rect x="1" y="2.5" width="8" height="5.5" stroke="#1c3a6b" fill="none"/><path d="M1 2.5l4 3 4-3" stroke="#1c3a6b" fill="none"/></svg>hello@kavro.com.au</li>
    </ul>

    <div class="brand">
      <div class="brand-name"><span class="brand-dot"></span>KAVRO International</div>
      <p class="tagline">Supply &amp; Management of Infrastructure &amp; Logistics</p>
    </div>

    <div class="footer-band" role="img" aria-label="Soft blue gradient footer band"></div>

    <footer class="footer-info">
      <p class="divisions">KAVRO Film Services<span class="sep"></span>KAVRO Pilot Escorts<span class="sep"></span>KAVRO Tour Management<br><span class="sep"></span>KAVRO Driver</p>
      <p class="parent">are divisions of KAVRO International Pty Ltd</p>
      <p class="registration">ACN 000 482 117&nbsp;&nbsp;ABN 00 000 482 117</p>
    </footer>
  </main>
</body>
</html>
```